Design a New Business Card for Our Company

We are looking for fresh, unique, and a modern business card that reflects our roots as digital marketing agency focused on SEM.

Industry/Entity Type

Marketing

Contact Information for Business Card

looking for very unique out of the box designs. clean and modern that compliments our logo

Requirements
Must have
• colors should match our logo
• Front should have name, address, email, and phone/fax of the person, phone/fax are the same number
• back should have our url

```html
<!DOCTYPE html>
<html lang="en">
<head>
<meta charset="utf-8">
<title>Clearpath Solutions – Business Card</title>
<link href="https://fonts.googleapis.com/css2?family=Arimo:wght@400;700&display=swap" rel="stylesheet">
<style>
  :root{
    --page:#eceef1;
    --card-white:#fbfcfd;
    --blue:#7fb3dc;
    --blue-deep:#4f8fc4;
    --blue-light:#a7d0ee;
    --grey:#c4c7cb;
    --grey-text:#9a9ea3;
    --name-blue:#5b9bd1;
    --white:#ffffff;
  }
  *{box-sizing:border-box;margin:0;padding:0}
  html,body{width:1200px;height:780px;overflow:hidden;background:var(--page);font-family:"Arimo",Arial,sans-serif}
  .canvas{position:relative;width:1200px;height:780px}
  .card{position:absolute;top:235px;width:540px;height:310px;border-radius:16px;overflow:hidden;
        box-shadow:0 2px 0 #d7dbe0,0 4px 0 #c9ced4,0 12px 26px rgba(40,60,90,.18)}
  .card-front{left:40px;background:var(--card-white)}
  .card-back{left:620px}
  .front-art{position:absolute;inset:0}
  .brand{position:absolute;left:30px;top:170px;display:flex;align-items:center;gap:10px}
  .brand-dot{width:24px;height:24px;border-radius:50%;background:var(--blue-deep)}
  .brand-name{font-weight:700;font-size:22px;color:var(--grey-text);letter-spacing:.3px;white-space:nowrap}
  .holder{position:absolute;right:28px;top:18px;text-align:right}
  .holder-name{font-weight:700;font-size:15px;color:var(--name-blue);letter-spacing:.5px;line-height:18px}
  .holder-role{font-size:11px;color:var(--grey-text);line-height:14px}
  .holder-phones{margin-top:6px;font-size:11px;color:var(--grey-text);line-height:16px}
  .contact{position:absolute;right:28px;top:126px;text-align:right;color:var(--white);font-size:11px;line-height:16.5px;white-space:nowrap}
  .contact .gap{height:10px}
  .line{display:flex;justify-content:flex-end;align-items:center;gap:6px}
  .icon{width:12px;height:12px;flex:none}
  .back-art{position:absolute;inset:0}
  .website{position:absolute;inset:0;display:flex;align-items:center;justify-content:center;
           color:var(--white);font-size:20px;letter-spacing:.5px}
</style>
</head>
<body>
<main class="canvas">

  <section class="card card-front" aria-label="Business card front">
    <svg class="front-art" viewBox="0 0 540 310" width="540" height="310" aria-hidden="true">
      <defs>
        <linearGradient id="waveBlue" x1="0" y1="0" x2="1" y2="1">
          <stop offset="0" stop-color="#8cc0e6"/>
          <stop offset="1" stop-color="#6ea7d6"/>
        </linearGradient>
      </defs>
      <path class="grey-band" d="M330 190 C312 245 280 295 170 310" fill="none" stroke="var(--grey)" stroke-width="9"/>
      <path class="blue-panel" d="M540 94 C420 94 372 112 352 160 C330 215 300 285 200 310 L540 310 Z" fill="url(#waveBlue)"/>
      <path class="blue-highlight" d="M540 104 C428 104 382 120 362 166 C342 220 314 288 222 310" fill="none" stroke="var(--blue-light)" stroke-width="3"/>
    </svg>

    <div class="brand">
      <span class="brand-dot"></span>
      <span class="brand-name">Clearpath Solutions</span>
    </div>

    <div class="holder">
      <div class="holder-name">DANIEL REYES</div>
      <div class="holder-role">Maneger</div>
      <div class="holder-phones">
        <div class="line">123 456 7890
          <svg class="icon" viewBox="0 0 13 13"><rect width="13" height="13" rx="2" fill="var(--name-blue)"/><path d="M4 3 L5.5 3 L6 5 L5 5.8 Q6 7.6 7.2 8 L8 7 L10 7.5 L10 9 Q6 10 3.5 5 Z" fill="#fff"/></svg>
        </div>
        <div class="line">123 456 7890
          <svg class="icon" viewBox="0 0 13 13"><rect width="13" height="13" rx="2" fill="var(--name-blue)"/><rect x="3" y="5" width="7" height="5" fill="#fff"/><rect x="4.5" y="2.5" width="4" height="3" fill="#fff"/></svg>
        </div>
      </div>
    </div>

    <div class="contact">
      <div>Your Address,2nd Ste</div>
      <div>Cedar Hollow, Texas 1234</div>
      <div class="gap"></div>
      <div class="line">123 456 7890
        <svg class="icon" viewBox="0 0 13 13"><rect width="13" height="13" rx="2" fill="#fff"/><path d="M4 3 L5.5 3 L6 5 L5 5.8 Q6 7.6 7.2 8 L8 7 L10 7.5 L10 9 Q6 10 3.5 5 Z" fill="var(--blue-deep)"/></svg>
      </div>
      <div class="line">123 456 7890
        <svg class="icon" viewBox="0 0 13 13"><rect width="13" height="13" rx="2" fill="#fff"/><rect x="3" y="5" width="7" height="5" fill="var(--blue-deep)"/><rect x="4.5" y="2.5" width="4" height="3" fill="var(--blue-deep)"/></svg>
      </div>
      <div class="line">your@yourcompany.com
        <svg class="icon" viewBox="0 0 13 13"><rect width="13" height="13" rx="2" fill="#fff"/><rect x="2.5" y="4" width="8" height="5.5" fill="none" stroke="var(--blue-deep)" stroke-width="1"/><path d="M2.5 4 L6.5 7 L10.5 4" fill="none" stroke="var(--blue-deep)" stroke-width="1"/></svg>
      </div>
    </div>
  </section>

  <section class="card card-back" aria-label="Business card back">
    <svg class="back-art" viewBox="0 0 540 310" width="540" height="310" role="img" aria-label="Soft blue gradient background where faint circle decoration sits">
      <defs>
        <radialGradient id="backGlow" cx="0.45" cy="0.45" r="0.75">
          <stop offset="0" stop-color="#86c0e3"/>
          <stop offset="1" stop-color="#4a86c0"/>
        </radialGradient>
      </defs>
      <rect width="540" height="310" fill="url(#backGlow)"/>
    </svg>
    <div class="website">www.yourwebsite.com</div>
  </section>

</main>
</body>
</html>
```